Portal for Beautiful & Up-and-Coming Caribbean destination of KVT, Puerto Rico

We need the web design of an online portal for the KVT community of Puerto Rico. This should include the landing page, menu page, and at least one content page. The KVT area is a vibrant area in Northwest Puerto Rico with an airport, many local restaurants, beautiful beaches, and many things to do. I attach the logo which should be featured prominently, and we'll also be selling merchandise using this logo. The website should be a place for everyone in the community or tourists looking for things to do and places to stay. It will need to feature space and places for advertising as well. Also, we have a live hashtag feed (www.kvtvibe-demo.com) where businesses and people in the community can hashtag their posts (we have licensed software that updates it every 30 minutes). We would like for the live hashtag feed to be part of the design, though the format can be changed a bit from what is currently in place. Indeed, the landing page should be changed to emphasize both the hashtag feed as well as the content of the site of KVTvibe. We need the landing page, menu page which will include 10-15 different modules or pages (examples: restaurants, things to do, places to stay, flights). I attach a spreadsheet which shows the menu pages that need to be featured. Comparable websites in our area are www.gosulena.com and www.varelaguide.com (but I don't like either one!). The final design should be contemporary, fresh, colorful fun and current, and communicate a vibrant and interactive community.

Target Market(s)

Tourists and people who live in this beach - oriented, beautiful community

Industry/Entity Type

Community

Number of Pages Required

3 page

Font styles to use
Sans Serif

Colors
33a6d7
f68e4e

Requirements
Must have
• landing page, menu design/page, and a sample content page. It must integrate a live hashtag feed, comparable to what is currently seen on www.kvtvibe-demo.com. It must be fun, contemporary, colorful, unique, and clean. It must allow for advertising space.
Nice to have
• comments and interaction with visitors. Colors that integrate with the logo. Much emphasis on the logo, as we will also be selling merchandise.
Should not have
• extra squiggles and curlies and adornments.

```html
<!DOCTYPE html>
<html lang="en">
<head>
<meta charset="utf-8">
<title>KVTvibe – Community Portal</title>
<link rel="stylesheet" href="https://fonts.googleapis.com/css2?family=Cinzel:wght@400;700&family=Lato:ital,wght@0,400;0,700;0,900;1,400&display=swap">
<style>
:root{
  --blue:#33a6d7;
  --orange:#f68e4e;
  --dark:#1d2831;
  --ink:#2b2b2b;
  --muted:#6f7780;
  --gray-band:#ebebeb;
  --footer:#1b252d;
  --line:#d9dde1;
}
*{box-sizing:border-box;margin:0;padding:0}
html,body{width:1200px;height:3956px;overflow:hidden}
body{font-family:"Lato",Arial,sans-serif;color:var(--ink);background:#fff;position:relative}
.abs{position:absolute}
.brand{font-family:"Lato",Arial,sans-serif;font-weight:900;color:var(--orange);letter-spacing:1px}
.brand-dot{display:inline-block;width:14px;height:14px;border-radius:50%;background:var(--blue);margin-right:8px;vertical-align:middle}

/* HERO */
.hero{position:absolute;left:0;top:0;width:1200px;height:610px;border-top:5px solid var(--orange);
  background:linear-gradient(180deg,#2a3642 0%,#3b4b57 45%,#52636b 70%,#2e3d48 100%);
  clip-path:polygon(0 0,100% 0,100% 527px,0 601px)}
.hero-photo{position:absolute;inset:0;background:linear-gradient(90deg,rgba(40,55,65,.2),rgba(90,110,120,.25) 50%,rgba(30,45,55,.2))}
.topbar-item{position:absolute;top:26px;display:flex;align-items:center;gap:10px;color:#fff;z-index:3}
.topbar-icon{width:26px;height:26px;border-radius:50%;background:var(--blue);display:flex;align-items:center;justify-content:center}
.topbar-item small{display:block;font-size:10px;color:var(--orange);font-weight:700}
.topbar-item strong{display:block;font-size:18px;font-weight:700}
.hero-logo{position:absolute;left:0;width:1200px;top:42px;text-align:center;font-size:40px;z-index:3}
.nav-item{position:absolute;width:264px;height:264px;margin:-132px 0 0 -132px;display:flex;flex-direction:column;align-items:center;justify-content:center;color:#fff;z-index:2;text-align:center;font-size:16px;line-height:1.2}
.nav-item::before{content:"";position:absolute;left:38.5px;top:38.5px;width:187px;height:187px;transform:rotate(45deg);background:var(--c);z-index:-1}
.nav-item svg{margin-bottom:12px}
.c-dark{--c:rgba(22,32,42,.72)}
.c-orange{--c:rgba(233,128,62,.88)}
.c-blue{--c:rgba(40,150,200,.85)}

/* SECTION TITLES */
.sec-title{position:absolute;left:0;width:1200px;text-align:center;font-family:"Cinzel",Georgia,serif;font-size:36px;font-weight:700;color:var(--ink)}
.sec-title span{color:var(--blue)}
.divider{position:absolute;left:450px;width:300px;height:20px}

/* HASHTAG FEED */
.tile{position:absolute;overflow:hidden}
.tile-caption{position:absolute;left:0;right:0;bottom:0;padding:8px 8px 6px;background:rgba(0,0,0,.55);color:#fff;font-size:12px}
.stats{display:flex;gap:12px;align-items:center;margin-top:3px;font-size:11px;font-weight:700}
.stats i{display:inline-flex;align-items:center;gap:4px;font-style:normal}
.feature-card{position:absolute;left:469px;top:905px;width:377px;height:147px;background:linear-gradient(180deg,#22313e,#1a2833);color:#fff;text-align:center;padding:16px 30px 0}
.feature-card p{font-weight:700;font-size:15px;line-height:1.3}
.feature-card .stats{justify-content:center;margin-top:8px}
.social-row{display:flex;gap:8px;justify-content:center;margin-top:10px}
.social-row b{width:22px;height:22px;border-radius:50%;display:block}
.ad-box{position:absolute;left:100px;top:1495px;width:1000px;height:124px;border:2px solid #cfd8de;display:flex;align-items:center;justify-content:center;font-family:"Cinzel",Georgia,serif;font-size:26px;font-weight:700;color:var(--ink)}

/* COMMUNITY BAND */
.orange-band{position:absolute;left:0;top:1630px;width:1200px;height:632px;background:var(--orange);clip-path:polygon(0 84px,100% 0,100% 553px,0 632px);z-index:2}
.band-title{position:absolute;font-family:"Cinzel",Georgia,serif;font-size:30px;font-weight:700;color:#fff}
.arrow-btn{position:absolute;top:1758px;width:18px;height:18px;border-radius:50%;background:#fff;display:flex;align-items:center;justify-content:center;z-index:3}
.arrow-btn::after{content:"";width:6px;height:6px;border-radius:50%;background:var(--blue)}
.blog-card{position:absolute;width:321px;height:142px;background:#fff;display:flex;z-index:3}
.blog-photo{width:160px;height:100%;position:relative}
.date-badge{position:absolute;right:-2px;top:8px;width:40px;height:44px;background:var(--blue);color:#fff;text-align:center;font-weight:900;font-size:18px;line-height:1;padding-top:6px}
.date-badge small{display:block;font-size:9px;font-weight:700}
.blog-body{flex:1;padding:12px 10px;position:relative}
.blog-body h4{font-size:13px;font-weight:900;margin-bottom:6px}
.blog-body p{font-size:10px;color:var(--muted);line-height:1.35}
.blog-meta{display:flex;gap:10px;margin-top:8px;font-size:10px;color:var(--muted)}
.blog-body::after{content:"";position:absolute;right:0;bottom:0;border-left:16px solid transparent;border-bottom:16px solid var(--dark)}
.calendar{position:absolute;left:841px;top:1812px;width:259px;height:160px;background:#fff;z-index:3;padding:14px 8px 6px}
.cal-tab{position:absolute;left:60px;top:-14px;width:139px;height:26px;background:var(--blue);color:#fff;font-size:13px;font-weight:700;text-align:center;line-height:26px}
.calendar table{width:100%;border-collapse:collapse;font-size:11px;text-align:center}
.calendar th{font-weight:900;font-size:10px;padding:3px 0;border-bottom:1px solid var(--line)}
.calendar td{padding:3px 0;color:#444}
.calendar td.off{color:#bbb}
.search-event{position:absolute;left:841px;top:1985px;width:259px;z-index:3;color:#fff}
.search-event label{font-size:14px;font-weight:700;display:block;margin-bottom:4px}
.date-field{height:26px;background:#fff;margin-bottom:6px;display:flex;justify-content:space-between;align-items:center;padding:0 6px;color:#999;font-size:11px}
.date-field b{width:20px;height:18px;background:#c9d0d5;display:block}
.search-btn{display:inline-flex;align-items:center;gap:6px;background:var(--blue);color:#fff;font-size:13px;font-weight:700;height:28px;padding:0 8px;margin-top:4px}

/* TRAVEL GUIDE */
.gray-band{position:absolute;left:0;top:2150px;width:1200px;height:600px;background:var(--gray-band);clip-path:polygon(0 0,100% 0,100% 450px,0 590px)}
.hub{position:absolute;left:509px;top:2387px;width:184px;height:184px;border-radius:50%;background:#fff;border:6px solid #f5f5f5;box-shadow:0 0 0 2px #e0e0e0;display:flex;align-items:center;justify-content:center;font-size:30px}
.guide-item{position:absolute;width:330px;font-size:12px;color:#444;line-height:1.35}
.guide-item h5{font-size:15px;font-weight:900;color:var(--ink);margin-bottom:3px}
.guide-item.left{text-align:right}
.guide-icon{position:absolute;top:2px;width:36px;height:36px;background:var(--blue);display:flex;align-items:center;justify-content:center}
.guide-icon.round{border-radius:50%}

/* TESTIMONIALS */
.quote-mark{position:absolute;font-family:Georgia,serif;font-size:90px;color:var(--orange);line-height:1}
.testimonial{position:absolute;left:230px;top:2912px;width:740px;text-align:center;font-style:italic;font-size:14px;color:var(--muted);line-height:1.55}
.avatar{position:absolute;border-radius:50%;background:linear-gradient(135deg,#c9a88a,#7b5e4a);border:4px solid #fff;box-shadow:0 0 0 2px #dfe3e6}
.avatar.active{box-shadow:0 0 0 3px var(--orange)}
.person{position:absolute;left:0;width:1200px;top:3134px;text-align:center;font-family:"Cinzel",Georgia,serif;font-weight:700;font-size:18px}
.dots{position:absolute;left:570px;top:3184px;display:flex;gap:8px}
.dots b{width:16px;height:16px;border-radius:50%;border:3px solid #cfd6db;display:block}
.dots b.on{border-color:var(--blue)}

/* NEWSLETTER */
.newsletter{position:absolute;left:0;top:3215px;width:1200px;height:270px;background:var(--blue);clip-path:polygon(0 75px,100% 0,100% 100%,0 100%)}
.news-figure{position:absolute;left:40px;top:3190px;width:230px;height:291px;border-radius:110px 110px 0 0;background:linear-gradient(180deg,#d7a460 0%,#c68f4e 30%,#2e4e8c 60%,#223f77 100%)}
.news-title{position:absolute;left:282px;top:3362px;font-family:"Cinzel",Georgia,serif;font-weight:700;font-size:25px;line-height:1.1;color:var(--dark)}
.news-input{position:absolute;left:488px;top:3370px;width:488px;height:48px;background:#fff;font-size:13px;color:#555;padding:0 12px;display:flex;align-items:center}
.news-submit{position:absolute;left:976px;top:3370px;width:118px;height:48px;background:var(--orange);color:#fff;font-weight:900;font-size:18px;display:flex;align-items:center;justify-content:center}

/* FOOTER */
.footer{position:absolute;left:0;top:3481px;width:1200px;height:343px;background:linear-gradient(180deg,#1f2b34,#172027)}
.footer-about{position:absolute;left:100px;top:3600px;width:310px;font-size:12px;color:#aab3ba;line-height:1.5}
.footer-head{position:absolute;top:3528px;color:#fff;font-size:19px;font-weight:700}
.footer-head::after{content:"";display:block;width:40px;height:3px;background:var(--orange);margin-top:8px}
.link-col{position:absolute;top:3595px;list-style:none;font-size:13px;color:#d2d8dc}
.link-col li{margin-bottom:12px}
.link-col li::before{content:"›";color:var(--orange);margin-right:8px;font-weight:900}
.contact-row{position:absolute;left:857px;display:flex;gap:14px;color:#d2d8dc;font-size:12px;line-height:1.4}
.contact-row strong{color:#fff;font-size:16px}
.bottom-strip{position:absolute;left:0;top:3824px;width:1200px;height:132px;background:#f1f1f1}
.bottom-social{position:absolute;left:0;width:1200px;top:3846px;display:flex;justify-content:center;gap:12px}
.bottom-social b{width:32px;height:32px;border-radius:50%;display:block}
.copyright{position:absolute;left:0;width:1200px;top:3920px;text-align:center;font-size:12px;color:#555}
</style>
</head>
<body>

<!-- HERO & MENU -->
<header class="hero">
  <div class="hero-photo" role="img" aria-label="Evening photo of the coastal town and harbour"></div>

  <div class="topbar-item" style="left:105px">
    <span class="topbar-icon"><svg width="14" height="14" viewBox="0 0 24 24"><path d="M6 2l4 4-2 3c1 3 4 6 7 7l3-2 4 4-3 4C10 22 2 14 2 5z" fill="#fff"/></svg></span>
    <span><small>call us today</small><strong>123 456 7890</strong></span>
  </div>
  <div class="hero-logo"><span class="brand"><span class="brand-dot"></span>KVTvibe</span></div>
  <div class="topbar-item" style="left:905px">
    <span class="topbar-icon"><svg width="14" height="14" viewBox="0 0 24 24"><rect x="2" y="5" width="20" height="14" fill="#fff"/><path d="M2 5l10 8 10-8" stroke="#33a6d7" stroke-width="2" fill="none"/></svg></span>
    <span><small>call us today</small><strong>inquiry@kvtvibe-demo.com</strong></span>
  </div>

  <nav>
    <a class="nav-item c-dark" style="left:192px;top:237px"><svg width="34" height="30" viewBox="0 0 34 30"><circle cx="24" cy="6" r="4" fill="#fff"/><path d="M2 24c5-4 10 4 15 0s10 4 15 0M6 18l10-8 6 6" stroke="#fff" stroke-width="3" fill="none"/></svg>Water<br>Activities</a>
    <a class="nav-item c-dark" style="left:453px;top:237px"><svg width="30" height="28" viewBox="0 0 30 28"><path d="M15 2L2 14h4v12h7v-8h4v8h7V14h4z" fill="#fff"/></svg>HOME</a>
    <a class="nav-item c-dark" style="left:717px;top:237px"><svg width="28" height="28" viewBox="0 0 28 28"><path d="M10 3L8 25M20 3l-2 22M4 10h21M3 18h21" stroke="#fff" stroke-width="3"/></svg>Hashtag<br>Feeds</a>
    <a class="nav-item c-dark" style="left:973px;top:237px"><svg width="28" height="30" viewBox="0 0 28 30"><rect x="4" y="2" width="20" height="26" stroke="#fff" stroke-width="2" fill="none"/><path d="M9 8h3M16 8h3M9 14h3M16 14h3M9 20h3M16 20h3" stroke="#fff" stroke-width="2"/></svg>Places<br>to Stay</a>

    <a class="nav-item c-dark" style="left:63px;top:369px"><svg width="30" height="32" viewBox="0 0 30 32"><path d="M6 2v10M10 2v10M14 2v10M6 12h8M10 12v18M22 2c-4 4-4 12 0 14v14" stroke="#fff" stroke-width="2.5" fill="none"/></svg>Restaurant<br>Service</a>
    <a class="nav-item c-orange" style="left:319px;top:369px"><svg width="40" height="30" viewBox="0 0 40 30"><path d="M2 18l8 2 6-6-10-10 4-1 14 8 10-4c3 0 3 3 0 4L10 26l-4-1 6-5-8-1z" fill="#fff"/></svg>Book<br>Flight</a>
    <a class="nav-item c-blue" style="left:583px;top:369px"><svg width="30" height="30" viewBox="0 0 30 30"><rect x="3" y="5" width="24" height="22" stroke="#fff" stroke-width="2" fill="none"/><path d="M3 11h24M9 2v6M21 2v6M8 16h3M14 16h3M20 16h3M8 21h3M14 21h3" stroke="#fff" stroke-width="2"/></svg>Latest<br>Events</a>
    <a class="nav-item c-orange" style="left:844px;top:369px"><svg width="32" height="30" viewBox="0 0 32 30"><rect x="2" y="8" width="28" height="20" stroke="#fff" stroke-width="2.5" fill="none"/><path d="M10 2l6 6 6-6" stroke="#fff" stroke-width="2.5" fill="none"/></svg>Live<br>Entertainment</a>
    <a class="nav-item c-blue" style="left:1094px;top:369px"><svg width="32" height="28" viewBox="0 0 32 28"><path d="M2 10c4-8 24-8 28 0l-5 4-4-4V7h-8v3l-4 4zM7 14h18l3 12H4z" fill="#fff"/></svg>Contact<br>Us</a>
  </nav>
</header>

<!-- LATEST HASHTAG POST -->
<h2 class="sec-title" style="top:622px">Latest <span>Hashtag Post</span></h2>
<svg class="divider" style="top:689px" viewBox="0 0 300 20"><path d="M0 10h132M168 10h132" stroke="#d3d8dc"/><circle cx="150" cy="10" r="7" stroke="#33a6d7" stroke-width="2.5" fill="none"/><circle cx="150" cy="10" r="2.5" fill="#33a6d7"/></svg>

<div class="tile" style="left:100px;top:746px;width:361px;height:306px;background:linear-gradient(160deg,#b9cfe2,#c9b79c 50%,#6d6b55)" role="img" aria-label="Wedding couple in front of a historic stone fort">
  <div class="tile-caption">Se está a organizar um casamento ou um evento<div class="stats"><i><svg width="12" height="11" viewBox="0 0 12 11"><path d="M6 10L1 5a3 3 0 015-3 3 3 0 015 3z" fill="#fff"/></svg>100</i><i><svg width="12" height="11" viewBox="0 0 12 11"><ellipse cx="6" cy="5" rx="5" ry="4" stroke="#fff" fill="none"/></svg>300</i></div></div>
</div>
<div class="tile" style="left:469px;top:746px;width:377px;height:151px;background:linear-gradient(180deg,#7fb4dc,#b48b72 60%,#9c6f5c)" role="img" aria-label="Group of friends waving a flag on the beach">
  <div class="tile-caption">Se está a organizar um casamento ou um evento<div class="stats"><i><svg width="12" height="11" viewBox="0 0 12 11"><path d="M6 10L1 5a3 3 0 015-3 3 3 0 015 3z" fill="#fff"/></svg>100</i><i><svg width="12" height="11" viewBox="0 0 12 11"><ellipse cx="6" cy="5" rx="5" ry="4" stroke="#fff" fill="none"/></svg>300</i></div></div>
</div>
<div class="feature-card" role="group" aria-label="Featured hashtag post">
  <p>Lorem ipsum dolor sit amet, more consectetuer adipiscing elit.</p>
  <div class="stats"><i><svg width="12" height="11" viewBox="0 0 12 11"><path d="M6 10L1 5a3 3 0 015-3 3 3 0 015 3z" fill="#fff"/></svg>100</i><i><svg width="12" height="11" viewBox="0 0 12 11"><ellipse cx="6" cy="5" rx="5" ry="4" stroke="#fff" fill="none"/></svg>300</i></div>
  <div class="social-row"><b style="background:#3bb4e8"></b><b style="background:#3b5998"></b><b style="background:#0e76a8"></b><b style="background:#dd4b39"></b><b style="background:#cb2027"></b><b style="background:#e52d27"></b><b style="background:#8a7a66"></b></div>
</div>
<div class="tile" style="left:854px;top:746px;width:246px;height:306px;background:linear-gradient(180deg,#8cbbe0,#e3e7ea 55%,#8a8a7a)" role="img" aria-label="Bride and groom beside a seaside lookout tower">
  <div class="tile-caption">Se está a organizar um<div class="stats"><i><svg width="12" height="11" viewBox="0 0 12 11"><path d="M6 10L1 5a3 3 0 015-3 3 3 0 015 3z" fill="#fff"/></svg>100</i><i><svg width="12" height="11" viewBox="0 0 12 11"><ellipse cx="6" cy="5" rx="5" ry="4" stroke="#fff" fill="none"/></svg>300</i></div></div>
</div>

<div class="tile" style="left:100px;top:1060px;width:554px;height:211px;background:linear-gradient(180deg,#8fc1e4,#5e9fc4 35%,#a77a5f 70%,#d9c3a0)" role="img" aria-label="Friends in swimwear posing on the beach">
  <div class="tile-caption">Se está a organizar um casamento ou um evento<div class="stats"><i><svg width="12" height="11" viewBox="0 0 12 11"><path d="M6 10L1 5a3 3 0 015-3 3 3 0 015 3z" fill="#fff"/></svg>100</i><i><svg width="12" height="11" viewBox="0 0 12 11"><ellipse cx="6" cy="5" rx="5" ry="4" stroke="#fff" fill="none"/></svg>300</i></div></div>
</div>
<div class="tile" style="left:662px;top:1060px;width:438px;height:211px;background:linear-gradient(135deg,#b95a3a,#e0a24a 45%,#8a3d3f)" role="img" aria-label="Friends in colourful carnival masks">
  <div class="tile-caption">Se está a organizar um casamento ou um evento<div class="stats"><i><svg width="12" height="11" viewBox="0 0 12 11"><path d="M6 10L1 5a3 3 0 015-3 3 3 0 015 3z" fill="#fff"/></svg>100</i><i><svg width="12" height="11" viewBox="0 0 12 11"><ellipse cx="6" cy="5" rx="5" ry="4" stroke="#fff" fill="none"/></svg>300</i></div></div>
</div>

<div class="tile" style="left:100px;top:1282px;width:327px;height:171px;background:linear-gradient(180deg,#6fb2e4,#d8e8ef 55%,#4f8a5a)" role="img" aria-label="Beach wedding setup with palm trees">
  <div class="tile-caption">Se está a organizar um casamento ou um evento<div class="stats"><i><svg width="12" height="11" viewBox="0 0 12 11"><path d="M6 10L1 5a3 3 0 015-3 3 3 0 015 3z" fill="#fff"/></svg>100</i><i><svg width="12" height="11" viewBox="0 0 12 11"><ellipse cx="6" cy="5" rx="5" ry="4" stroke="#fff" fill="none"/></svg>300</i></div></div>
</div>
<div class="tile" style="left:435px;top:1282px;width:330px;height:171px;background:linear-gradient(135deg,#c4362a,#e8b33a 40%,#2f7f6a 75%,#b8502e)" role="img" aria-label="Colourful carnival costumes">
  <div class="tile-caption">Se está a organizar um casamento ou um evento<div class="stats"><i><svg width="12" height="11" viewBox="0 0 12 11"><path d="M6 10L1 5a3 3 0 015-3 3 3 0 015 3z" fill="#fff"/></svg>100</i><i><svg width="12" height="11" viewBox="0 0 12 11"><ellipse cx="6" cy="5" rx="5" ry="4" stroke="#fff" fill="none"/></svg>300</i></div></div>
</div>
<div class="tile" style="left:773px;top:1282px;width:327px;height:171px;background:linear-gradient(180deg,#3d8fb8,#5fb0c9 50%,#b99171)" role="img" aria-label="Snorkelers smiling in the sea">
  <div class="tile-caption">Se está a organizar um casamento ou um evento<div class="stats"><i><svg width="12" height="11" viewBox="0 0 12 11"><path d="M6 10L1 5a3 3 0 015-3 3 3 0 015 3z" fill="#fff"/></svg>100</i><i><svg width="12" height="11" viewBox="0 0 12 11"><ellipse cx="6" cy="5" rx="5" ry="4" stroke="#fff" fill="none"/></svg>300</i></div></div>
</div>

<div class="ad-box">Advertisement Will Come here</div>

<!-- GRAY TRAVEL BAND (behind orange) -->
<div class="gray-band"></div>

<!-- COMMUNITY BLOG & EVENTS -->
<div class="orange-band"></div>
<h3 class="band-title" style="left:100px;top:1745px;z-index:3">Community Blog/Reviews</h3>
<span class="arrow-btn" style="left:746px"></span>
<span class="arrow-btn" style="left:768px"></span>
<h3 class="band-title" style="left:841px;top:1745px;font-size:27px;z-index:3">Event &amp; Calendar</h3>

<article class="blog-card" style="left:100px;top:1820px">
  <div class="blog-photo" style="background:linear-gradient(160deg,#6fa7c4,#c7b79a)" role="img" aria-label="Surfer splashing in the waves"><span class="date-badge">29<small>Aug</small></span></div>
  <div class="blog-body"><h4>Lorem Ipsum Dolor Sit</h4><p>Lorem ipsum dolor sit amet, sec adipiscing elit, sed diam nonummy nibh euismod tincidunt ut.</p><div class="blog-meta"><span>♡ 2</span><span>◌ 0</span></div></div>
</article>
<article class="blog-card" style="left:467px;top:1820px">
  <div class="blog-photo" style="background:linear-gradient(180deg,#79b9e2,#5aa6c8 45%,#d8c39c)" role="img" aria-label="Friends jumping on the beach"><span class="date-badge">29<small>Aug</small></span></div>
  <div class="blog-body"><h4>Lorem Ipsum Dolor Sit</h4><p>Lorem ipsum dolor sit amet, sec adipiscing elit, sed diam nonummy nibh euismod tincidunt ut.</p><div class="blog-meta"><span>♡ 2</span><span>◌ 0</span></div></div>
</article>
<article class="blog-card" style="left:100px;top:1978px">
  <div class="blog-photo" style="background:linear-gradient(180deg,#8cc2e8,#d4c4a4 55%,#6f8b5a)" role="img" aria-label="Historic lookout on the coast"><span class="date-badge">29<small>Aug</small></span></div>
  <div class="blog-body"><h4>Lorem Ipsum Dolor Sit</h4><p>Lorem ipsum dolor sit amet, sec adipiscing elit, sed diam nonummy nibh euismod tincidunt ut.</p><div class="blog-meta"><span>♡ 2</span><span>◌ 0</span></div></div>
</article>
<article class="blog-card" style="left:467px;top:1978px">
  <div class="blog-photo" style="background:linear-gradient(180deg,#94c6e4,#c69a7c 55%,#6d7f6c)" role="img" aria-label="Couple standing outdoors"><span class="date-badge">29<small>Aug</small></span></div>
  <div class="blog-body"><h4>Lorem Ipsum Dolor Sit</h4><p>Lorem ipsum dolor sit amet, sec adipiscing elit, sed diam nonummy nibh euismod tincidunt ut.</p><div class="blog-meta"><span>♡ 2</span><span>◌ 0</span></div></div>
</article>

<div class="calendar">
  <span class="cal-tab">August 2016</span>
  <table>
    <tr><th>SUN</th><th>MON</th><th>TUE</th><th>WED</th><th>THU</th><th>FRI</th><th>SAT</th></tr>
    <tr><td>1</td><td>2</td><td>3</td><td>4</td><td>5</td><td>6</td><td>7</td></tr>
    <tr><td>8</td><td>9</td><td>10</td><td>11</td><td>12</td><td>13</td><td>14</td></tr>
    <tr><td>15</td><td>16</td><td>17</td><td>18</td><td>19</td><td>20</td><td>21</td></tr>
    <tr><td>22</td><td>23</td><td>24</td><td>25</td><td>26</td><td>27</td><td>28</td></tr>
    <tr><td>29</td><td>30</td><td>31</td><td class="off">1</td><td class="off">2</td><td class="off">3</td><td class="off">4</td></tr>
  </table>
</div>
<div class="search-event">
  <label>Search Event</label>
  <div class="date-field">To<b></b></div>
  <div class="date-field">From<b></b></div>
  <span class="search-btn">Search Now <svg width="14" height="14" viewBox="0 0 14 14"><circle cx="6" cy="6" r="4" stroke="#fff" stroke-width="2" fill="none"/><path d="M9 9l4 4" stroke="#fff" stroke-width="2"/></svg></span>
</div>

<!-- TRAVEL GUIDE & TIPS -->
<h2 class="sec-title" style="top:2268px">Travel <span>Guide &amp; Tips</span></h2>
<svg class="divider" style="top:2335px" viewBox="0 0 300 20"><path d="M0 10h132M168 10h132" stroke="#cfd4d8"/><circle cx="150" cy="10" r="7" stroke="#33a6d7" stroke-width="2.5" fill="none"/><circle cx="150" cy="10" r="2.5" fill="#33a6d7"/></svg>
<svg class="abs" style="left:380px;top:2400px" width="440" height="170" viewBox="0 0 440 170"><path d="M30 21h60l40 40M30 150h60l40-40M410 21h-60l-40 40M410 150h-60l-40-40" stroke="#c8cdd1" fill="none"/></svg>
<div class="hub"><span class="brand"><span class="brand-dot"></span>KVTvibe</span></div>

<div class="guide-item left" style="left:35px;top:2404px"><h5>Plan Your Travel</h5>Nunc cursus libero purus ac congue arcu cursus massa dignite requietam elerisque mi.</div>
<span class="guide-icon" style="left:372px;top:2406px"><svg width="18" height="18" viewBox="0 0 18 18"><rect x="3" y="2" width="12" height="14" stroke="#fff" stroke-width="2" fill="none"/><path d="M6 7h6M6 11h6" stroke="#fff" stroke-width="2"/></svg></span>
<div class="guide-item left" style="left:35px;top:2534px"><h5>Check Availability</h5>Nunc cursus libero purus ac congue arcu cursus massa dignite requietam elerisque mi.</div>
<span class="guide-icon" style="left:372px;top:2536px"><svg width="18" height="18" viewBox="0 0 18 18"><rect x="2" y="3" width="14" height="13" stroke="#fff" stroke-width="2" fill="none"/><path d="M2 7h14M6 1v4M12 1v4" stroke="#fff" stroke-width="2"/></svg></span>

<span class="guide-icon round" style="left:790px;top:2406px"><svg width="18" height="18" viewBox="0 0 18 18"><path d="M2 8h4v8H2zM7 8l4-6c2 0 2 2 1 4h4c1 0 2 1 1 3l-2 6H7z" fill="#fff"/></svg></span>
<div class="guide-item" style="left:836px;top:2404px"><h5>Easy Booking System</h5>Nunc cursus libero purus ac congue arcu cursus massa dignite requietam elerisque mi.</div>
<span class="guide-icon round" style="left:790px;top:2536px;color:#fff;font-weight:900;font-size:18px">$</span>
<div class="guide-item" style="left:836px;top:2534px"><h5>Flight + Hotel Savings</h5>Nunc cursus libero purus ac congue arcu cursus massa dignite requietam elerisque mi.</div>

<!-- TESTIMONIALS -->
<h2 class="sec-title" style="top:2776px">What People <span>Say About Us</span></h2>
<svg class="divider" style="top:2843px" viewBox="0 0 300 20"><path d="M0 10h132M168 10h132" stroke="#d3d8dc"/><circle cx="150" cy="10" r="7" stroke="#33a6d7" stroke-width="2.5" fill="none"/><circle cx="150" cy="10" r="2.5" fill="#33a6d7"/></svg>
<span class="quote-mark" style="left:190px;top:2880px">“</span>
<p class="testimonial">Lorem ipsum dolor sit amet, consectetuer adipiscing elit, sed diam nonummy nibh euismod tincidunt ut laoreet dolore magna aliquam erat volutpat. Ut wisi enim ad minim veniam, quis nostrud exer tation ullamcorper suscipit lobortis nisl ut aliquip laoreet consequat. Duis autem vel dolor in hendrerit in vulputate velit esse.</p>
<span class="quote-mark" style="left:940px;top:2940px">”</span>
<svg class="abs" style="left:250px;top:3010px" width="700" height="14" viewBox="0 0 700 14"><path d="M0 2h340l10 10 10-10h340" stroke="#d3d8dc" fill="#fff"/></svg>
<span class="avatar" role="img" aria-label="Portrait of a reviewer" style="left:496px;top:3056px;width:62px;height:62px"></span>
<span class="avatar active" role="img" aria-label="Portrait of the featured reviewer" style="left:584px;top:3050px;width:74px;height:74px;background:linear-gradient(135deg,#e2b890,#8c6248)"></span>
<span class="avatar" role="img" aria-label="Portrait of a reviewer" style="left:686px;top:3056px;width:62px;height:62px;background:linear-gradient(135deg,#d9b48f,#6f5140)"></span>
<div class="person">Mara Quintel</div>
<div class="dots"><b class="on"></b><b></b><b></b></div>

<!-- NEWSLETTER -->
<div class="newsletter"></div>
<div class="news-figure" role="img" aria-label="Woman in a sun hat looking at the sea"></div>
<h3 class="news-title">Subscribe to<br>Newsletter</h3>
<div class="news-input">Please Type Your Email</div>
<div class="news-submit">SUBMIT</div>

<!-- FOOTER -->
<footer class="footer"></footer>
<div class="abs" style="left:100px;top:3530px;font-size:34px"><span class="brand"><span class="brand-dot"></span>KVTvibe</span></div>
<p class="footer-about">Ut wisi enim ad minim veniam, quis nostrud exerci tation more ullamcorper suscipit lobortis nis ut aliquip commodo consequat. Duis autem iriure dolor in hendrerit in vulputate veessent molestie consequat, vel illum facilisi. Lorem ipsum dolor sit amet, conse ctetuer adipiscing elit, sedmod di nonummy nibh commodo consequat.</p>

<h4 class="footer-head" style="left:448px">Quick Links</h4>
<ul class="link-col" style="left:448px"><li>Home</li><li>Events</li><li>Hashtag</li><li>Services</li><li>Blog</li><li>Contact Us</li></ul>
<ul class="link-col" style="left:580px"><li>Map of Beaches</li><li>Historical Sites</li><li>Real Estate</li><li>Shopping</li><li>Weather Reports</li><li>Science</li></ul>
<ul class="link-col" style="left:725px"><li>Place to Stay</li><li>Restaurants</li><li>Live<br>&nbsp;&nbsp;&nbsp;Entertainment</li><li>Water<br>&nbsp;&nbsp;&nbsp;Activites</li></ul>

<h4 class="footer-head" style="left:857px">Contact Informations</h4>
<div class="contact-row" style="top:3595px"><svg width="20" height="26" viewBox="0 0 20 26"><path d="M10 1a8 8 0 00-8 8c0 6 8 16 8 16s8-10 8-16a8 8 0 00-8-8z" fill="#f68e4e"/><circle cx="10" cy="9" r="3" fill="#1b252d"/></svg><span>Vista Mar<br>111/2, Calle Sol, lorem,<br>City Code 1234</span></div>
<div class="contact-row" style="top:3675px"><svg width="20" height="20" viewBox="0 0 24 24"><path d="M6 2l4 4-2 3c1 3 4 6 7 7l3-2 4 4-3 4C10 22 2 14 2 5z" fill="#f68e4e"/></svg><span>Call us<br><strong>123 - 456 - 7890</strong></span></div>
<div class="contact-row" style="top:3740px"><svg width="22" height="18" viewBox="0 0 22 18"><rect x="1" y="2" width="20" height="14" fill="#f68e4e"/><path d="M1 2l10 8 10-8" stroke="#1b252d" stroke-width="2" fill="none"/></svg><span>Email Us<br><strong>info@kvtvibe-demo.com</strong></span></div>

<div class="bottom-strip"></div>
<div class="bottom-social"><b style="background:#3bb4e8"></b><b style="background:#3b5998"></b><b style="background:#0e76a8"></b><b style="background:#cb2027"></b><b style="background:#dd4b39"></b><b style="background:#e52d27"></b><b style="background:#8a7a66"></b></div>
<p class="copyright">Copyright © 2016 KVTvibe. All Rights Reserved</p>

</body>
</html>
```